"Tolvar" (spanish restaurant) "Bar de Tapas"

"Tolvar" is a spanish restaurant located in the city of Santo Domingo, Dominican Republic. It needs a new and fresh idea for its business card. I would like to take the idea of one of the spaces of the restaurant represented on a business card, for example, the blue and emblematic entrance door of the restaurant, or maybe the bricks on the main room of the restaurant, or how about the bar. Any idea it's good! I invite all the creative designers to participate on the suggestions of it.

What doe sit need? It needs this information on it:

Name: Tolvar
Business: Restaurante
Address: Ruth P Caldera 00, Bellavento
Phone number: 809-555-0147
website: www.tolvarrestaurante.example

Reason: NEED MORE OPTION FOR IT. I WANT YOU TO EXPRESS YOUR DESIGN AS YOU WANT TO NOT AS I ASK YOU TO.

Industry/Entity Type

Restaurant

Contact Information for Business Card

c/Ruth P Caldera 47

Requirements
Must have
• Creativity. I'm open to new and fresh ideas.
Nice to have
• The entrance door (blue one) would be a plus in the design of the card. Maybe the background could be images of materials like bricks or wood, like the ones in the pictures of the restaurant.

```html
<!DOCTYPE html>
<html lang="es">
<head>
<meta charset="utf-8">
<title>Tolvar — Business Card</title>
<link href="https://fonts.googleapis.com/css2?family=Montserrat:wght@500;600&display=swap" rel="stylesheet">
<style>
  :root {
    --backdrop: #d9d9d7;
    --card: #0f0f0f;
    --card-edge: #1c1c1c;
    --accent: #e8262a;
    --text: #ffffff;
    --rule: #2a2a2a;
  }
  * { margin: 0; padding: 0; box-sizing: border-box; }
  html, body { width: 1200px; height: 900px; overflow: hidden; }
  body {
    background: var(--backdrop);
    font-family: "Montserrat", sans-serif;
    position: relative;
  }
  .card {
    position: absolute;
    width: 560px;
    height: 320px;
    background: radial-gradient(ellipse at 40% 35%, var(--card-edge), var(--card) 70%);
    border-radius: 4px;
    box-shadow: 0 10px 24px rgba(0,0,0,.25);
  }
  .card--back { left: 520px; top: 110px; }
  .card--front { left: 120px; top: 450px; }

  .brand-name {
    color: var(--text);
    font-weight: 600;
    letter-spacing: 2px;
    line-height: 1;
  }
  .brand-tag {
    color: var(--text);
    font-weight: 500;
    text-transform: uppercase;
    line-height: 1;
  }

  .card--back .brand {
    position: absolute; inset: 0;
    display: flex; flex-direction: column; align-items: center; justify-content: center;
    gap: 8px;
  }
  .card--back .brand-name { font-size: 50px; }
  .card--back .brand-tag { font-size: 11px; letter-spacing: 3px; }
  .card--back .brand-tag--below { letter-spacing: 5px; }

  .holder { position: absolute; left: 36px; top: 112px; }
  .holder-name { color: var(--accent); font-size: 22px; font-weight: 500; letter-spacing: .5px; }
  .holder-role { color: var(--text); font-size: 13px; font-weight: 500; margin-top: 4px; }

  .divider {
    position: absolute; left: 36px; right: 36px; top: 176px;
    height: 1px; background: var(--rule);
  }

  .card--front .brand {
    position: absolute; right: 36px; top: 34px;
    display: flex; flex-direction: column; align-items: center; gap: 6px;
  }
  .card--front .brand-row { display: flex; align-items: center; gap: 10px; }
  .brand-mark { width: 18px; height: 18px; background: var(--accent); }
  .card--front .brand-name { color: var(--accent); font-size: 36px; }
  .card--front .brand-tag { color: var(--accent); font-size: 9px; letter-spacing: 3px; }

  .contact {
    position: absolute; right: 36px; bottom: 22px;
    list-style: none; text-align: right;
  }
  .contact li {
    color: var(--text); font-size: 14px; font-weight: 500;
    line-height: 24px;
    display: flex; justify-content: flex-end; align-items: center; gap: 10px;
  }
  .contact svg { width: 12px; height: 12px; fill: none; stroke: var(--accent); stroke-width: 2; flex: none; }
</style>
</head>
<body>
  <section class="card card--back">
    <div class="brand">
      <span class="brand-tag">Bar de Tapas</span>
      <span class="brand-name">Tolvar</span>
      <span class="brand-tag brand-tag--below">Restaurante</span>
    </div>
  </section>

  <section class="card card--front">
    <div class="holder">
      <p class="holder-name">Daniel Reyes</p>
      <p class="holder-role">Managing Director</p>
    </div>

    <div class="brand">
      <span class="brand-tag">Bar de Tapas</span>
      <div class="brand-row">
        <span class="brand-mark"></span>
        <span class="brand-name">Tolvar</span>
      </div>
      <span class="brand-tag">Restaurante</span>
    </div>

    <div class="divider"></div>

    <ul class="contact">
      <li>809-555-0147
        <svg viewBox="0 0 12 12" aria-hidden="true"><rect x="3" y="1" width="6" height="10" rx="1"/></svg>
      </li>
      <li>c/Ruth P Caldera 47, Bellavento
        <svg viewBox="0 0 12 12" aria-hidden="true"><path d="M6 11 C3 7.5 2 6 2 4.5 A4 4 0 0 1 10 4.5 C10 6 9 7.5 6 11 Z"/><circle cx="6" cy="4.5" r="1.2"/></svg>
      </li>
      <li>hola@tolvarrestaurante.example
        <svg viewBox="0 0 12 12" aria-hidden="true"><rect x="1" y="3" width="10" height="7"/><path d="M1 3 L6 7 L11 3"/></svg>
      </li>
      <li>www.tolvarrestaurante.example
        <svg viewBox="0 0 12 12" aria-hidden="true"><path d="M5 7 L7 5"/><rect x="1" y="6" width="5" height="3" rx="1.5" transform="rotate(-45 3.5 7.5)"/><rect x="6" y="3" width="5" height="3" rx="1.5" transform="rotate(-45 8.5 4.5)"/></svg>
      </li>
    </ul>
  </section>
</body>
</html>
```